Consulting Company PowerPoint Template Design

We are looking for an updated PowerPoint template design or our 55 person energy consulting firm (K7) based in San Francisco (www.kayseven.example). We would like two versions of the same PowerPoint template in a 16:9 and 4:3 format with our existing logo.

We have an existing color scheme and template and are seeking your help to polish/update the template design for wide format and create a flexible template that is easy to use with content from Excel and Word. Our current template, and a couple of examples that we like are attached.

Specific requests include:

• Dark background for slide title
• A narrow section header
• Maximizing white space for content
• A limited number of well designed Master template layouts to choose from
• A selection of title and section header slides that are not San Francisco specific with some variety to chose from ideally with a focus on energy or nature, graphics/visuals.

For examples of energy specific templates see:
https://www.brightslidery.example/energy/powerpoint-templates/0.html

Requirements
Must have
• Must use our logo but open to other designs, fonts, and styles for the PowerPoint template.
• Please use our existing color scheme found in the attached Excel file.
• Also we would like the ability to easily copy and paste from our existing/original template to the new template. In other words we would like backward compatibility to apply the new template format to our old PowerPoints that use our existing template.

```html
<!DOCTYPE html>
<html lang="en">
<head>
<meta charset="utf-8">
<title>K7 Energy Consulting – Presentation Template Layouts</title>
<link rel="stylesheet" href="https://fonts.googleapis.com/css2?family=Signika:wght@300;400;600;700&display=swap">
<style>
:root{
  --navy:#1a4f75;
  --navy-deep:#143f5e;
  --gold:#c9a85a;
  --gold-soft:#d8bd74;
  --white:#ffffff;
  --ink:#3c4a55;
  --red:#b5321a;
  --green:#1f8a3c;
  --indigo:#1c2a80;
  --blue-text:#1a4f75;
  --board:#e3e3e3;
}
*{box-sizing:border-box;margin:0;padding:0}
html,body{width:857px;height:1200px;overflow:hidden}
body{background:radial-gradient(circle at 50% 45%,#f2f2f2 0%,var(--board) 70%,#d6d6d6 100%);font-family:"Signika",sans-serif;color:var(--ink)}
.board{position:relative;width:857px;height:1200px;display:grid;grid-template-columns:repeat(3,243px);grid-auto-rows:182px;column-gap:14px;row-gap:15.5px;padding:13px 0 0 50px}
.slide{position:relative;width:243px;height:182px;overflow:hidden;background:var(--white);box-shadow:0 1px 4px rgba(0,0,0,.28)}
.slide.dark{background:var(--navy)}
.slide.closing{grid-column:2}

/* brand strip on title slides */
.brand-strip{position:absolute;left:0;top:0;width:100%;height:34px;background:var(--white);border-bottom:2px solid var(--gold);display:flex;align-items:center;padding-left:20px;gap:4px}
.brand-dot{width:16px;height:16px;border-radius:50%;background:var(--navy);flex:none}
.brand-name{font-size:5px;font-weight:600;color:var(--navy)}

/* header band */
.hdr{position:absolute;left:0;top:0;width:100%;height:27px;background:var(--navy);border-bottom:2px solid var(--gold);display:flex;align-items:center;justify-content:space-between;padding:0 16px 0 18px}
.hdr-title{font-size:8.5px;font-weight:600;color:var(--white)}
.mark{display:flex;align-items:center;gap:2px;font-size:4.5px;font-weight:600;color:var(--white)}
.mark::before{content:"";width:6px;height:6px;border-radius:50%;border:1px solid var(--white)}
.mark-float{position:absolute;right:10px;top:8px;width:14px;height:14px;border-radius:50%;background:var(--navy);border:1px solid var(--white);font-size:4.5px;font-weight:600;color:var(--white);display:flex;align-items:center;justify-content:center}

.url{position:absolute;left:18px;bottom:6px;font-size:3.6px;color:var(--navy)}
.url.light{color:var(--white)}
.url.center{left:0;right:0;text-align:center}
.page{position:absolute;right:18px;bottom:5px;font-size:5px;font-weight:700;color:var(--navy)}
.page.light{color:var(--white)}

.title{font-size:10.5px;font-weight:600;color:var(--white);line-height:1.25;text-transform:uppercase}
.lede{font-size:4px;line-height:1.45;color:var(--white);font-weight:300}
.body{font-size:4px;line-height:1.5;color:var(--ink);font-weight:300}
.sub{font-size:5px;color:var(--gold);font-weight:400;margin-bottom:2px}

.ph{position:absolute}
.photo-circle{position:absolute;border-radius:50%;border:1.5px solid var(--gold)}

.icon-ring{position:absolute;width:38px;height:38px;border-radius:50%;border:1px solid var(--gold);display:flex;align-items:center;justify-content:center}
.col-text{position:absolute;width:65px;text-align:justify}

.stack{position:absolute;left:111px;top:43px;width:110px}
.stack .item{margin-bottom:6px}
.stack .label{font-size:4.4px;font-weight:600}
.stack .copy{font-size:4.4px;font-weight:600;color:var(--ink);line-height:1.3}

.tile{position:absolute;top:69px;width:68px;height:64px;padding:5px 6px;border-radius:2px}
.tile-title{font-size:4.8px;font-weight:600;color:var(--gold-soft);padding-bottom:3px;border-bottom:.6px solid rgba(255,255,255,.45);margin-bottom:3px}
.tile .body{color:var(--white)}

.num{position:absolute;width:20px;height:20px;display:flex;align-items:center;justify-content:center;font-size:6px;color:var(--white)}
.step{position:absolute;width:85px}
.step-title{font-size:6px;color:var(--ink);margin-bottom:1px}
.step.right{text-align:right}
</style>
</head>
<body>
<main class="board">

  <!-- Title: city lights -->
  <section class="slide dark">
    <div class="brand-strip"><span class="brand-dot"></span><span class="brand-name">K7 Energy Consulting</span></div>
    <div style="position:absolute;left:22px;top:78px;width:100px">
      <h1 class="title">Presentation Title<br>Goes Here</h1>
      <p class="lede" style="margin-top:4px;text-align:justify">Lorem ipsum dolor sit amet, consectetur adipiscing elit, sed do eiusmod tempor incididunt ut labore et dolore magna aliqua.</p>
    </div>
    <div class="photo-circle" role="img" aria-label="City skyline at night with light trails" style="left:145px;top:85px;width:124px;height:124px;background:linear-gradient(160deg,#2d5a9a 0%,#183a6a 45%,#7a5a3a 75%,#e0c090 100%)"></div>
    <span class="url light" style="left:22px">www.kayseven.example</span>
  </section>

  <!-- Title: wind turbine -->
  <section class="slide dark">
    <div class="brand-strip"><span class="brand-dot"></span><span class="brand-name">K7 Energy Consulting</span></div>
    <div style="position:absolute;left:22px;top:76px;width:100px">
      <h1 class="title">Presentation Title<br>Goes Here</h1>
      <p class="lede" style="margin-top:4px;text-align:justify">Lorem ipsum dolor sit amet, consectetur adipiscing elit, sed do eiusmod tempor incididunt ut labore et dolore magna aliqua.</p>
    </div>
    <div class="photo-circle" role="img" aria-label="Wind turbine above green hills at sunset" style="left:145px;top:82px;width:124px;height:124px;background:linear-gradient(180deg,#e7c9a8 0%,#b99a86 40%,#6c6a4a 62%,#7aa23a 80%,#5c8a2a 100%)"></div>
    <span class="url light" style="left:22px">www.kayseven.example</span>
  </section>

  <!-- Title: solar panel backdrop -->
  <section class="slide dark">
    <div class="brand-strip"><span class="brand-dot"></span><span class="brand-name">K7 Energy Consulting</span></div>
    <div class="ph" role="img" aria-label="Close-up of solar panels tinted blue" style="left:0;top:36px;width:100%;height:146px;background:linear-gradient(135deg,#2a6590 0%,#1a4f75 50%,#123c5c 100%)"></div>
    <div style="position:absolute;left:0;right:0;top:85px;text-align:center">
      <h1 class="title">Presentation Title<br>Goes Here</h1>
      <p class="lede" style="margin-top:4px">Lorem ipsum dolor sit amet, consectetur<br>adipiscing elit, sed do eiusmod tempor incididunt.</p>
    </div>
    <span class="url light center">www.kayseven.example</span>
  </section>

  <!-- Title: water backdrop -->
  <section class="slide dark">
    <div class="brand-strip"><span class="brand-dot"></span><span class="brand-name">K7 Energy Consulting</span></div>
    <div class="ph" role="img" aria-label="Water droplets splashing, tinted blue" style="left:0;top:36px;width:100%;height:146px;background:radial-gradient(ellipse at 75% 30%,#3f7da6 0%,#24608a 40%,#1a4f75 100%)"></div>
    <div style="position:absolute;left:0;right:0;top:84px;text-align:center">
      <h1 class="title">Presentation Title<br>Goes Here</h1>
      <p class="lede" style="margin-top:4px">Lorem ipsum dolor sit amet, consectetur<br>adipiscing elit, sed do eiusmod tempor incididunt.</p>
    </div>
    <span class="url light center">www.kayseven.example</span>
  </section>

  <!-- Heading only -->
  <section class="slide">
    <header class="hdr"><h2 class="hdr-title">Heading Text Goes Here</h2><span class="mark">K7</span></header>
    <span class="url">www.kayseven.example</span><span class="page">01</span>
  </section>

  <!-- Heading + circle image -->
  <section class="slide">
    <header class="hdr"><h2 class="hdr-title">Heading Text Goes Here</h2><span class="mark">K7</span></header>
    <div class="photo-circle" role="img" aria-label="Ocean wave breaking" style="left:15px;top:62px;width:58px;height:58px;border:none;background:linear-gradient(180deg,#1d4f6a 0%,#2f8aa3 45%,#cfe4ea 70%,#f2f4f5 100%)"></div>
    <div style="position:absolute;left:83px;top:68px;width:142px">
      <p class="sub">Subheading text goes here</p>
      <p class="body" style="text-align:justify">Lorem ipsum dolor sit amet, consectetur adipiscing elit, sed do eiusmod tempor incididunt ut labore et dolore magna aliqua. Ut enim ad minim veniam, quis nostrud exercitation ullamco laboris nisi ut aliquip ex ea commodo consequat.</p>
    </div>
    <span class="url">www.kayseven.example</span><span class="page">01</span>
  </section>

  <!-- Heading + three icons -->
  <section class="slide">
    <header class="hdr"><h2 class="hdr-title">Heading Text Goes Here</h2><span class="mark">K7</span></header>
    <div class="icon-ring" style="left:23px;top:57px">
      <svg width="18" height="10" viewBox="0 0 18 10"><rect x="1" y="1" width="14" height="8" fill="none" stroke="#1a4f75" stroke-width="1.4"/><rect x="15" y="3.5" width="2" height="3" fill="#1a4f75"/><rect x="3" y="3" width="7" height="4" fill="#1a4f75"/></svg>
    </div>
    <div class="icon-ring" style="left:102px;top:57px">
      <svg width="18" height="18" viewBox="0 0 18 18"><circle cx="9" cy="9" r="7" fill="none" stroke="#1a4f75" stroke-width="1.3"/><ellipse cx="9" cy="9" rx="3" ry="7" fill="none" stroke="#1a4f75" stroke-width="1"/><line x1="2" y1="9" x2="16" y2="9" stroke="#1a4f75" stroke-width="1"/></svg>
    </div>
    <div class="icon-ring" style="left:181px;top:57px">
      <svg width="12" height="18" viewBox="0 0 12 18"><path d="M6 1a5 5 0 0 0-3 9v3h6v-3a5 5 0 0 0-3-9z" fill="none" stroke="#1a4f75" stroke-width="1.3"/><line x1="4" y1="15.5" x2="8" y2="15.5" stroke="#1a4f75" stroke-width="1.3"/></svg>
    </div>
    <p class="col-text body" style="left:10px;top:107px">Lorem ipsum dolor sit amet, consectetur adipiscing elit, sed do eiusmod tempor incididunt ut labore et dolore magna aliqua. Ut enim ad minim veniam.</p>
    <p class="col-text body" style="left:89px;top:107px">Lorem ipsum dolor sit amet, consectetur adipiscing elit, sed do eiusmod tempor incididunt ut labore et dolore magna aliqua. Ut enim ad minim veniam.</p>
    <p class="col-text body" style="left:168px;top:107px">Lorem ipsum dolor sit amet, consectetur adipiscing elit, sed do eiusmod tempor incididunt ut labore et dolore magna aliqua. Ut enim ad minim veniam.</p>
    <span class="url">www.kayseven.example</span><span class="page">01</span>
  </section>

  <!-- Heading + photo + subheading list -->
  <section class="slide">
    <header class="hdr"><h2 class="hdr-title">Heading Text Goes Here</h2><span class="mark">K7</span></header>
    <div class="ph" role="img" aria-label="Electricity pylon against a cloudy sky" style="left:27px;top:40px;width:74px;height:118px;background:linear-gradient(180deg,#6f8fb8 0%,#a9bcd2 45%,#5f7390 80%,#3b4a5c 100%)"></div>
    <div class="stack">
      <div class="item"><p class="label" style="color:var(--navy)">Subheading goes here</p><p class="copy">Lorem ipsum dolor sit amet,<br>consectetur adipisicing elit</p></div>
      <div class="item"><p class="label" style="color:var(--gold)">Subheading goes here</p><p class="copy">Lorem ipsum dolor sit amet,<br>consectetur adipisicing elit</p></div>
      <div class="item"><p class="label" style="color:var(--red)">Subheading goes here</p><p class="copy">Lorem ipsum dolor sit amet,<br>consectetur adipisicing elit</p></div>
      <div class="item"><p class="label" style="color:var(--green)">Subheading goes here</p><p class="copy">Lorem ipsum dolor sit amet,<br>consectetur adipisicing elit</p></div>
    </div>
    <span class="url">www.kayseven.example</span><span class="page">01</span>
  </section>

  <!-- Section: water ripple -->
  <section class="slide dark">
    <div class="ph" role="img" aria-label="Ripples on calm blue water" style="left:0;top:0;width:100%;height:100%;background:radial-gradient(ellipse at 55% 75%,#2f6b93 0%,#1d5379 40%,#163f5e 100%)"></div>
    <div class="ph" style="left:0;top:0;width:100%;height:29px;background:rgba(20,63,94,.6)"></div>
    <span class="mark" style="position:absolute;right:16px;top:10px">K7</span>
    <div style="position:absolute;left:71px;top:64px;width:110px">
      <h2 class="title" style="color:var(--gold-soft);font-size:9.5px">Section Title Text<br>Goes Here</h2>
      <p class="lede" style="margin-top:4px">Lorem ipsum dolor sit amet, consectetur adipiscing elit, sed do eiusmod tempor incididunt ut labore et dolore magna aliqua.</p>
    </div>
    <span class="url light center">www.kayseven.example</span>
  </section>

  <!-- Section: light bulb -->
  <section class="slide">
    <div class="ph" role="img" aria-label="Glowing light bulb on warm golden background" style="left:0;top:0;width:100%;height:100%;background:radial-gradient(circle at 60% 60%,#e6d08f 0%,#d3b56a 45%,#c4a154 100%)"></div>
    <span class="mark-float">K7</span>
    <div style="position:absolute;left:71px;top:63px;width:110px">
      <h2 class="title" style="color:#1e5a7a;font-size:9.5px">Section Title Text<br>Goes Here</h2>
      <p class="lede" style="margin-top:4px;color:#f6ecd0">Lorem ipsum dolor sit amet, consectetur adipiscing elit, sed do eiusmod tempor incididunt ut labore et dolore magna aliqua.</p>
    </div>
    <span class="url light center">www.kayseven.example</span>
  </section>

  <!-- Heading + wide photo band -->
  <section class="slide">
    <header class="hdr"><h2 class="hdr-title">Heading Text Goes Here</h2><span class="mark">K7</span></header>
    <div class="ph" role="img" aria-label="Wind turbine nacelle with the moon behind" style="left:0;top:29px;width:100%;height:66px;background:linear-gradient(180deg,#6e7275 0%,#9a9d9c 55%,#c9cbc8 100%)"></div>
    <div style="position:absolute;left:45px;top:110px;width:152px">
      <p class="sub">Subheading text goes here</p>
      <p class="body" style="text-align:justify">Lorem ipsum dolor sit amet, consectetur adipiscing elit, sed do eiusmod tempor incididunt ut labore et dolore magna aliqua. Ut enim ad minim veniam, quis nostrud exercitation ullamco laboris nisi ut aliquip ex ea commodo consequat.</p>
    </div>
    <span class="url">www.kayseven.example</span><span class="page">01</span>
  </section>

  <!-- Heading + three coloured tiles -->
  <section class="slide">
    <header class="hdr"><h2 class="hdr-title">Heading Text Goes Here</h2><span class="mark">K7</span></header>
    <div class="ph" role="img" aria-label="Power lines at dusk over a dark landscape" style="left:0;top:29px;width:100%;height:71px;background:linear-gradient(180deg,#3f5f7a 0%,#8c8a8a 55%,#d38a4a 78%,#3a3a3a 100%)"></div>
    <div class="tile" style="left:7px;background:var(--red)"><p class="tile-title">CREATIVE TITLE</p><p class="body">Lorem ipsum dolor sit amet, consectetur adipiscing elit, sed do eiusmod tempor incididunt ut labore et.</p></div>
    <div class="tile" style="left:86px;background:var(--green)"><p class="tile-title">CREATIVE TITLE</p><p class="body">Lorem ipsum dolor sit amet, consectetur adipiscing elit, sed do eiusmod tempor incididunt ut labore et.</p></div>
    <div class="tile" style="left:163px;background:var(--indigo)"><p class="tile-title">CREATIVE TITLE</p><p class="body">Lorem ipsum dolor sit amet, consectetur adipiscing elit, sed do eiusmod tempor incididunt ut labore et.</p></div>
    <span class="url">www.kayseven.example</span><span class="page">01</span>
  </section>

  <!-- Heading + half photo + text -->
  <section class="slide">
    <header class="hdr"><h2 class="hdr-title">Heading Text Goes Here</h2><span class="mark">K7</span></header>
    <div class="ph" role="img" aria-label="Single wind turbine in a field under a cloudy sky" style="left:0;top:29px;width:111px;height:153px;background:linear-gradient(180deg,#9fb3c7 0%,#d8dee3 45%,#b9b39d 75%,#8a6a3a 100%)"></div>
    <div style="position:absolute;left:126px;top:41px;width:104px">
      <p class="body" style="font-weight:600;font-size:4.4px;color:#1f2a33;margin-bottom:4px">Lorem ipsum dolor sit amet, consectetur adipiscing elit, sed do eiusmod tempor incididunt ut labore et dolore magna aliqua.</p>
      <p class="body">Ut enim ad minim veniam, quis nostrud exercitation ullamco laboris nisi ut aliquip ex ea commodo consequat. Duis aute irure dolor in reprehenderit in voluptate velit esse cillum dolore eu fugiat nulla pariatur. Excepteur sint occaecat cupidatat non proident, sunt in culpa qui officia deserunt mollit anim id est laborum.</p>
    </div>
    <span class="page">01</span>
  </section>

  <!-- Heading + numbered steps -->
  <section class="slide">
    <header class="hdr"><h2 class="hdr-title">Heading Text Goes Here</h2><span class="mark">K7</span></header>
    <div class="step right" style="left:5px;top:61px"><p class="step-title">Title here</p><p class="body">Lorem ipsum dolor sit amet<br>consectetur adipiscing elit sed.</p></div>
    <span class="num" style="left:94px;top:60px;background:var(--navy)">01</span>
    <span class="num" style="left:128px;top:60px;background:var(--red)">02</span>
    <div class="step" style="left:153px;top:61px"><p class="step-title">Title here</p><p class="body">Lorem ipsum dolor sit amet<br>consectetur adipiscing elit sed.</p></div>
    <div class="step right" style="left:5px;top:113px"><p class="step-title">Title here</p><p class="body">Lorem ipsum dolor sit amet<br>consectetur adipiscing elit sed.</p></div>
    <span class="num" style="left:94px;top:112px;background:var(--green)">03</span>
    <span class="num" style="left:128px;top:112px;background:var(--gold)">04</span>
    <div class="step" style="left:153px;top:113px"><p class="step-title">Title here</p><p class="body">Lorem ipsum dolor sit amet<br>consectetur adipiscing elit sed.</p></div>
    <span class="url">www.kayseven.example</span><span class="page">01</span>
  </section>

  <!-- Heading over photo + text panel -->
  <section class="slide dark">
    <div class="ph" role="img" aria-label="Rows of solar panels under a bright cloudy sky" style="left:0;top:0;width:100%;height:97px;background:linear-gradient(180deg,#bcd0e4 0%,#e8eef2 30%,#5a7fb0 55%,#2a4c86 100%)"></div>
    <h2 class="hdr-title" style="position:absolute;left:18px;top:9px;color:var(--gold-soft);opacity:.85">Heading Text Goes Here</h2>
    <span class="mark-float">K7</span>
    <p class="lede" style="position:absolute;left:34px;top:111px;width:182px;text-align:justify;font-size:4.4px">Lorem ipsum dolor sit amet, consectetur adipiscing elit, sed do eiusmod tempor incididunt ut labore et dolore magna aliqua. Ut enim ad minim veniam, quis nostrud exercitation ullamco laboris nisi ut aliquip ex ea commodo consequat. Duis aute irure dolor in reprehenderit in voluptate velit esse cillum.</p>
    <span class="url light">www.kayseven.example</span><span class="page light">01</span>
  </section>

  <!-- Closing -->
  <section class="slide dark closing">
    <div class="brand-strip"><span class="brand-dot"></span><span class="brand-name">K7 Energy Consulting</span></div>
    <h1 class="title" style="position:absolute;left:20px;top:93px;font-size:14px;text-transform:none">THANK YOU!</h1>
    <div class="photo-circle" role="img" aria-label="City skyline at night with light trails" style="left:145px;top:83px;width:124px;height:124px;background:linear-gradient(160deg,#2d5a9a 0%,#183a6a 45%,#7a5a3a 75%,#e0c090 100%)"></div>
    <span class="url light" style="left:22px">www.kayseven.example</span>
  </section>

</main>
</body>
</html>
```